brixolanemark.com needs a good website design and logo

Our company sells memberships to a website that generates systematic rules-based investment strategies on a monthly basis.
I would like a modern professional wordpress design that uses the color blue. It should communicate financial safety and growth. The company is based in Denver Colorado USA.
Please see current website: https://www.brixolanemark.com

Target Market(s)

individual investors looking to improve their investment performance. Looking for improved returns or ways to limit losses.

Industry/Entity Type

Investment

Logo Text

brixolaneMark

Coding

Coded - Design and coding required

Font styles to use
Sans Serif

Colors
3176b5
85abd2
0355a3
00a990

Requirements
Must have
• I've included details in the attached document.
• The colors selected below are suggestions. While we want the color blue, please use the best version of blue you think is good.
Nice to have
• The design with work with wordpress. We would like to be able to modify the theme later using elementor and a base theme, like maybe astra?
• There is additional work to be done after this contest including designing other pages.
• The site uses some plovexura.com to display charts and investment performance, if you have experience making these charts and graphs look good, that would be valuable.

```html
<!DOCTYPE html>
<html lang="en">
<head>
<meta charset="UTF-8">
<title>brixolaneMark — Investment Strategies</title>
<link href="https://fonts.googleapis.com/css2?family=Mulish:wght@400;600;700;800&family=Lato:wght@400;700&display=swap" rel="stylesheet">
<style>
:root{
  --navy:#0e3a8f;
  --navy-dark:#0a2c6e;
  --blue:#1f78b6;
  --teal:#16a58b;
  --ink:#333842;
  --muted:#6d7280;
  --grey-bg:#efefef;
  --line:#cfd3d8;
  --white:#ffffff;
}
*{box-sizing:border-box;margin:0;padding:0}
html,body{width:1200px;height:2946px;overflow:hidden}
body{font-family:"Lato",sans-serif;color:var(--ink);background:var(--white);position:relative}
.section{position:absolute;left:0;width:1200px}
.center{text-align:center}

/* Header */
.site-header{top:0;height:94px;background:var(--white)}
.brand{position:absolute;display:flex;align-items:center;gap:10px;font-family:"Mulish",sans-serif;font-weight:800;color:var(--navy)}
.brand-mark{background:var(--teal);display:block}
.site-header .brand{left:153px;top:24px;font-size:30px}
.site-header .brand-mark{width:40px;height:40px}
.main-nav a{position:absolute;top:32px;font-family:"Mulish",sans-serif;font-weight:700;font-size:17px;color:var(--navy);text-decoration:none}
.btn{display:inline-flex;align-items:center;justify-content:center;border-radius:30px;font-family:"Mulish",sans-serif;font-weight:700;text-decoration:none;position:absolute}
.btn-login{left:915px;top:26px;width:126px;height:43px;background:linear-gradient(#2260b4,var(--navy));color:var(--white);font-size:15px}

/* Hero */
.hero{top:94px;height:589px;background:linear-gradient(115deg,#132b4a 0%,#1d4771 45%,#123458 75%,#0b2440 100%);overflow:hidden}
.hero-art{position:absolute;inset:0}
.hero h1{position:absolute;top:175px;width:100%;font-family:"Mulish",sans-serif;font-weight:600;font-size:44px;color:var(--white);letter-spacing:.5px}
.hero h2{position:absolute;top:230px;width:100%;font-family:"Mulish",sans-serif;font-weight:700;font-size:36px;line-height:43px;color:var(--white)}
.btn-teal{background:var(--teal);color:var(--white)}
.hero .btn{left:503px;top:348px;width:184px;height:51px;font-size:17px}

/* About */
.about{top:683px;height:370px}
.section-title{position:absolute;width:100%;font-family:"Mulish",sans-serif;font-weight:800;font-size:31px}
.about .section-title{top:62px;color:var(--ink)}
.about .section-title span{color:var(--teal)}
.about p{position:absolute;left:177px;top:130px;width:872px;font-size:15px;line-height:23px;color:#444}
.btn-outline{left:530px;top:256px;width:163px;height:42px;border:2px solid var(--navy);color:var(--navy);font-size:15px}

/* Features */
.features{top:1053px;height:397px;background:var(--grey-bg)}
.feature{position:absolute;top:82px;width:285px;height:248px;background:var(--white);text-align:center;padding:0 26px}
.feature svg{margin-top:30px}
.feature p{margin-top:14px;font-size:15px;line-height:24px;color:var(--muted)}
.feature.is-active{background:var(--navy)}
.feature.is-active p{color:#e6ecf7}
.feature-next{position:absolute;left:119px;bottom:-25px;width:48px;height:48px;border-radius:50%;background:var(--navy);border:2px solid var(--white);display:flex;align-items:center;justify-content:center}

/* Pricing */
.pricing{top:1450px;height:577px}
.pricing .section-title{top:36px;color:var(--navy)}
.plan{position:absolute;top:109px;width:273px;height:374px;background:var(--white);box-shadow:0 6px 18px rgba(0,0,0,.18);text-align:center}
.plan-head{height:96px;background:linear-gradient(90deg,#1f77b6,#149d8f);position:relative;color:var(--white);font-family:"Mulish",sans-serif;font-weight:700;font-size:19px;line-height:23px;padding-top:16px}
.plan-head svg{position:absolute;left:0;bottom:-1px}
.plan-price{font-family:"Mulish",sans-serif;font-weight:700;color:var(--teal);font-size:40px;height:62px;line-height:50px}
.plan-price sup{font-size:20px;vertical-align:top;line-height:30px}
.plan ul{list-style:none;width:206px;margin:0 auto}
.plan li{font-size:17px;color:var(--muted);height:42px;line-height:40px;border-bottom:2px solid var(--line)}
.plan li:last-child{border-bottom:none}
.plan .btn{left:38px;bottom:26px;width:197px;height:43px;background:var(--navy);color:var(--white);font-size:14px}

/* Blog */
.blog{top:2027px;height:520px;background:var(--grey-bg)}
.blog .section-title{top:54px;color:var(--teal)}
.post{position:absolute;top:120px;width:274px}
.post-image{width:274px;height:220px}
.post h3{margin-top:28px;font-family:"Mulish",sans-serif;font-weight:600;font-size:21px;line-height:27px;color:#222}
.post-meta{margin-top:12px;font-size:13px;color:#444;display:flex;align-items:center;gap:6px}
.post-meta i{display:inline-block;width:10px;height:10px;background:var(--teal);border-radius:2px}
.post-meta .sep{margin:0 6px}

/* CTA */
.cta{top:2547px;height:242px;background:linear-gradient(90deg,#123b8c,#1a4fa3 50%,#123b8c)}
.cta p{position:absolute;top:66px;width:100%;font-family:"Mulish",sans-serif;font-size:27px;line-height:30px;color:var(--white)}
.cta .btn{left:524px;top:148px;width:175px;height:47px;font-size:17px}

/* Footer */
.site-footer{top:2789px;height:157px}
.site-footer .brand{left:172px;top:58px;font-size:26px}
.site-footer .brand-mark{width:34px;height:34px}
.footer-nav a{position:absolute;top:58px;font-family:"Mulish",sans-serif;font-weight:600;font-size:16px;color:#555;text-decoration:none}
.copyright{position:absolute;left:436px;top:84px;font-size:13px;color:#777}
.social{position:absolute;top:54px;width:32px;height:32px;border-radius:50%;background:var(--navy)}
</style>
</head>
<body>

<header class="section site-header">
  <div class="brand"><span class="brand-mark"></span>brixolaneMark</div>
  <nav class="main-nav">
    <a href="#" style="left:501px">ABOUT</a>
    <a href="#" style="left:599px">PRICING</a>
    <a href="#" style="left:705px">BLOG</a>
    <a href="#" style="left:788px">CONTACT</a>
  </nav>
  <a class="btn btn-login" href="#">LOG IN</a>
</header>

<section class="section hero">
  <div class="hero-art" role="img" aria-label="Dark blue photo of stacked coins with a glowing rising stock chart"></div>
  <svg class="hero-art" width="1200" height="589" viewBox="0 0 1200 589" aria-hidden="true">
    <polyline points="0,500 150,430 300,470 450,360 560,410 700,300 820,380 940,160 1050,260 1200,70" fill="none" stroke="#25d1b9" stroke-width="3" opacity=".8"/>
    <polyline points="0,560 200,520 380,540 520,470 680,500 850,380 1000,420 1200,230" fill="none" stroke="#1fb7c9" stroke-width="2" opacity=".6"/>
  </svg>
  <h1 class="center">WIN MORE, LOSE LESS</h1>
  <h2 class="center">Investment strategies that boost<br>returns and limit risk.</h2>
  <a class="btn btn-teal" href="#">SIGN UP FREE</a>
</section>

<section class="section about">
  <h2 class="section-title center">ABOUT <span>BRIXOLANEMARK</span></h2>
  <p class="center">Aliquam molestie, mi et imperdiet euismod, dui purus auctor tellus, et interdum lacus lectus et ante. Sed accumsan sollicitudin sapien, sit amet adipiscing turpis gravida ac. In congue, neque ac lobortis volutpat, libero mauris varius mi, vitae suscipit ipsum ligula vitae risus. Duis aliquam nibh a dui iaculis viverra id a velit. Vivamus egestas risus in magna varius commodo. Sed semper viverra egestas. Etiam pretium porttitor lectus, vel ornare neque porta volutpat.</p>
  <a class="btn btn-outline" href="#">READ MORE</a>
</section>

<section class="section features">
  <div class="feature" style="left:165px">
    <svg width="44" height="50" viewBox="0 0 44 50" fill="none" stroke="#0e3a8f" stroke-width="2"><circle cx="22" cy="20" r="15"/><ellipse cx="22" cy="20" rx="6" ry="15"/><line x1="7" y1="20" x2="37" y2="20"/><rect x="10" y="38" width="24" height="10"/></svg>
    <p>When you can't afford to lose, our model portfolios can protect investments by reducing holdings to risky assets when the market turns down.</p>
  </div>
  <div class="feature is-active" style="left:464px">
    <svg width="46" height="46" viewBox="0 0 46 46" fill="none" stroke="#ffffff" stroke-width="2"><circle cx="23" cy="23" r="20"/><path d="M23 23V3M23 23L40 33"/><circle cx="32" cy="32" r="7"/></svg>
    <p>Our dynamic portfolios find the best places to invest. They adjust monthly to invest in the strongest funds.</p>
    <span class="feature-next"><svg width="24" height="18" viewBox="0 0 24 18" fill="none" stroke="#fff" stroke-width="2"><path d="M1 9H22M14 1L22 9L14 17"/></svg></span>
  </div>
  <div class="feature" style="left:762px">
    <svg width="44" height="44" viewBox="0 0 44 44" fill="none" stroke="#0e3a8f" stroke-width="2"><rect x="3" y="14" width="38" height="26"/><path d="M3 14L22 28L41 14"/><rect x="12" y="4" width="20" height="16"/></svg>
    <p>You receive monthly email recommendations generated from our systematic, rules-based models.</p>
  </div>
</section>

<section class="section pricing">
  <h2 class="section-title center">OUR PRICING</h2>
  <div class="plan" style="left:159px">
    <div class="plan-head">LIMITED FREE<br>MEMBERSHIP<svg width="273" height="40" viewBox="0 0 273 40" preserveAspectRatio="none"><path d="M0 40Q136 -10 273 40Z" fill="#fff"/></svg></div>
    <div class="plan-price">FREE</div>
    <ul><li>Basic Strategies</li><li>Trends Tracker</li></ul>
    <a class="btn" href="#">FREE MEMBERSHP</a>
  </div>
  <div class="plan" style="left:462px">
    <div class="plan-head">MONTHLY<br>MEMBERSHIP<svg width="273" height="40" viewBox="0 0 273 40" preserveAspectRatio="none"><path d="M0 40Q136 -10 273 40Z" fill="#fff"/></svg></div>
    <div class="plan-price"><sup>$</sup>19<sup>95</sup></div>
    <ul><li>Basic Strategies</li><li>Advanced Strategies</li><li>Trends Tracker</li></ul>
    <a class="btn" href="#">MONTHLY MEMBERSHIP</a>
  </div>
  <div class="plan" style="left:764px">
    <div class="plan-head">ANNUAL<br>MEMBERSHIP<svg width="273" height="40" viewBox="0 0 273 40" preserveAspectRatio="none"><path d="M0 40Q136 -10 273 40Z" fill="#fff"/></svg></div>
    <div class="plan-price"><sup>$</sup>149<sup>95</sup></div>
    <ul><li>Basic Strategies</li><li>Advanced Strategies</li><li>Trends Tracker</li></ul>
    <a class="btn" href="#">ANNUAL MEMBERSHIP</a>
  </div>
</section>

<section class="section blog">
  <h2 class="section-title center">LATEST BLOG</h2>
  <article class="post" style="left:163px">
    <div class="post-image" role="img" aria-label="Photo of a tablet showing charts beside a cup of coffee" style="background:linear-gradient(135deg,#5a3a2c,#b8a79a 55%,#3a2a22)"></div>
    <h3>At vero eos et accusamus et iusto odio dignissi</h3>
    <div class="post-meta"><i></i>05/12/2018<span class="sep">|</span><i></i>Dana Morrow</div>
  </article>
  <article class="post" style="left:464px">
    <div class="post-image" role="img" aria-label="Photo of a laptop and printed charts on a desk" style="background:linear-gradient(135deg,#6b5448,#d8d4cf 55%,#8a7466)"></div>
    <h3>At vero eos et accusamus et iusto odio dignissi</h3>
    <div class="post-meta"><i></i>05/12/2018<span class="sep">|</span><i></i>Dana Morrow</div>
  </article>
  <article class="post" style="left:766px">
    <div class="post-image" role="img" aria-label="Photo of a team reviewing financial reports at a table" style="background:linear-gradient(135deg,#4a3c34,#c9c3b8 55%,#e8e6e0)"></div>
    <h3>At vero eos et accusamus et iusto odio dignissi</h3>
    <div class="post-meta"><i></i>05/12/2018<span class="sep">|</span><i></i>Dana Morrow</div>
  </article>
</section>

<section class="section cta">
  <p class="center">Worried about recent stock market volatility?<br>Learn how our momentum strategies can protect against loses.</p>
  <a class="btn btn-teal" href="#">FREE SIGN UP</a>
</section>

<footer class="section site-footer">
  <div class="brand"><span class="brand-mark"></span>brixolaneMark</div>
  <nav class="footer-nav">
    <a href="#" style="left:436px">ABOUT</a>
    <a href="#" style="left:526px">PRICING</a>
    <a href="#" style="left:622px">BLOG</a>
    <a href="#" style="left:699px">CONTACT</a>
  </nav>
  <div class="copyright">© 2018 Company Name&nbsp; All right reserved</div>
  <span class="social" style="left:881px" aria-label="Social link"></span>
  <span class="social" style="left:920px" aria-label="Social link"></span>
  <span class="social" style="left:959px" aria-label="Social link"></span>
  <span class="social" style="left:998px" aria-label="Social link"></span>
</footer>

</body>
</html>
```